Property management company looking for modern card design

We at Blue Heron Partners provides property management services for its residential and commercial properties, with expertise in all categories of multifamily, industrial and office projects throughout California.

We need a business card design that is professional and modern designed business card. In our field, clients get hundreds of business cards, we would like our card to stand out.

Please avoid small print.

Target Market(s)

Professionals and high end clients

Industry/Entity Type

Financial Planning

Contact Information for Business Card

Company Name: Blue Heron Partners, Name, email, license #, phone number, website blueheronpartners.com

Font styles to use
Sans Serif

Requirements
Must have
• The card design needs to be adaptable because there is a possibly we will be expanding into different sectors other than real estate. The card design should be focused on financial planning and asset management.
Nice to have
• Modern and simple business card. Eye catching. Non-standard size/shaped cards would be great.
• blueheronpartners.com
Should not have
• Too many bright color or any pictures or shapes of real estate stuff.

```html
<!DOCTYPE html>
<html lang="en">
<head>
<meta charset="utf-8">
<title>Blue Heron Partners – Business Card</title>
<link rel="stylesheet" href="https://fonts.googleapis.com/css2?family=Montserrat:wght@300;600;700&family=Source+Sans+3:wght@400;600&display=swap">
<style>
  :root {
    --backdrop: #d9d9d9;
    --paper: #ecebea;
    --wood-dark: #2b1711;
    --wood-mid: #4a2a1f;
    --wood-warm: #5e3426;
    --brand-ink: #3a2119;
    --ink-light: #ffffff;
    --ink-soft: #e6ddd8;
    --screw: #3a3a3a;
    --band: rgba(255,255,255,0.16);
  }
  * { box-sizing: border-box; margin: 0; padding: 0; }
  html, body { width: 1200px; height: 900px; overflow: hidden; }
  body {
    background: var(--backdrop);
    display: flex; flex-direction: column; align-items: center; justify-content: center;
    gap: 40px;
    font-family: "Source Sans 3", sans-serif;
  }
  .card {
    width: 700px; height: 400px;
    display: flex; position: relative;
    box-shadow: 0 10px 30px rgba(0,0,0,0.18);
  }
  .card__brand {
    width: 300px; height: 100%;
    background: var(--paper);
    position: relative;
    display: flex; align-items: center; justify-content: center;
    gap: 12px;
  }
  .brand__mark {
    width: 18px; height: 18px; flex: none;
    background: var(--brand-ink);
  }
  .brand__name {
    font-family: "Montserrat", sans-serif;
    font-weight: 600;
    font-size: 21px;
    color: var(--brand-ink);
    white-space: nowrap;
  }
  .screw {
    position: absolute; width: 12px; height: 12px; border-radius: 50%;
    background: var(--screw);
  }
  .screw--tl { top: 14px; left: 14px; }
  .screw--tr { top: 14px; right: 14px; }
  .screw--bl { bottom: 14px; left: 14px; }
  .screw--br { bottom: 14px; right: 14px; }
  .card__wood {
    flex: 1; height: 100%; position: relative;
    background: linear-gradient(100deg, var(--wood-mid) 0%, var(--wood-dark) 40%, var(--wood-warm) 70%, var(--wood-dark) 100%);
  }
  .contact {
    position: absolute; inset: 0;
    padding: 48px 40px 0 40px;
    color: var(--ink-light);
  }
  .contact__name {
    font-family: "Montserrat", sans-serif; font-weight: 700;
    font-size: 26px; text-transform: uppercase; letter-spacing: 0.5px;
  }
  .contact__title {
    font-family: "Montserrat", sans-serif; font-weight: 300;
    font-size: 24px; text-transform: uppercase; margin-bottom: 30px;
  }
  .contact__list { list-style: none; }
  .contact__item {
    display: flex; align-items: center; gap: 24px;
    font-size: 18px; color: var(--ink-soft);
    margin-bottom: 22px;
  }
  .contact__item svg { width: 24px; height: 24px; flex: none; }
  .band {
    position: absolute; left: 0; right: 0; bottom: 62px; height: 44px;
    background: var(--band);
    display: flex; align-items: center; justify-content: flex-end;
    padding-right: 34px;
    color: var(--ink-soft); font-size: 18px; letter-spacing: 0.5px;
  }
</style>
</head>
<body>

<section class="card card--front">
  <div class="card__brand">
    <span class="screw screw--tl"></span><span class="screw screw--tr"></span>
    <span class="screw screw--bl"></span><span class="screw screw--br"></span>
    <span class="brand__mark"></span>
    <span class="brand__name">Blue Heron Partners</span>
  </div>
  <div class="card__wood" role="img" aria-label="Dark wood grain texture">
    <div class="contact">
      <h1 class="contact__name">Daniel R Ortega</h1>
      <p class="contact__title">President/CEO</p>
      <ul class="contact__list">
        <li class="contact__item">
          <svg viewBox="0 0 24 24" fill="#fff"><path d="M6.6 10.8a15.1 15.1 0 0 0 6.6 6.6l2.2-2.2a1 1 0 0 1 1-.25 11.4 11.4 0 0 0 3.6.57 1 1 0 0 1 1 1V20a1 1 0 0 1-1 1A17 17 0 0 1 3 4a1 1 0 0 1 1-1h3.5a1 1 0 0 1 1 1c0 1.250.2 2.45.57 3.57a1 1 0 0 1-.25 1z"/></svg>
          (555) 014-2290
        </li>
        <li class="contact__item">
          <svg viewBox="0 0 24 24" fill="none" stroke="#fff" stroke-width="1.8"><rect x="2.5" y="5" width="19" height="14"/><path d="M2.5 5l9.5 8 9.5-8"/></svg>
          info@blueheronpartners.com
        </li>
        <li class="contact__item">
          <svg viewBox="0 0 24 24" fill="none" stroke="#fff" stroke-width="1.6"><circle cx="12" cy="12" r="9"/><ellipse cx="12" cy="12" rx="4" ry="9"/><path d="M3 12h18M5 7h14M5 17h14"/></svg>
          www.blueheronpartners.com
        </li>
        <li class="contact__item">
          <svg viewBox="0 0 24 24" fill="none" stroke="#fff" stroke-width="1.6"><rect x="2.5" y="5" width="19" height="14" rx="1"/><circle cx="8" cy="11" r="2" fill="#fff"/><path d="M5 16c.5-2 5.5-2 6 0M13.5 10h5M13.5 13h5"/></svg>
          4821-07-3316
        </li>
      </ul>
    </div>
  </div>
</section>

<section class="card card--back">
  <div class="card__brand">
    <span class="screw screw--tl"></span><span class="screw screw--tr"></span>
    <span class="screw screw--bl"></span><span class="screw screw--br"></span>
    <span class="brand__mark"></span>
    <span class="brand__name">Blue Heron Partners</span>
  </div>
  <div class="card__wood" role="img" aria-label="Dark wood grain texture">
    <div class="band">www.blueheronpartners.com</div>
  </div>
</section>

</body>
</html>
```